Single-sided business card for restaurant bellwether with new logo made on this site

Business card options with new logo including restaurant name, address, phone number and website. This business card is single-sided only and will be presented at the hostess desk for clients to take. I would like to see options based on a cream card background, a white card background, a yellow card background and a burgundy colored background. It needs to be elegant and traditional.

Target Market(s)

local and international crowd

Industry/Entity Type

restaurant

Contact Information for Business Card

address, website and phone number

Font styles to use
Serif

Colors
EE7325
F08F49
F5BC92
FAE3D3
FDF4ED

Requirements
Must have
• new logo, address, phone number, website
Should not have
• more than three colors

```html
<!DOCTYPE html>
<html lang="es">
<head>
<meta charset="utf-8">
<title>Bellwether business card options</title>
<link rel="stylesheet" href="https://fonts.googleapis.com/css2?family=Cinzel:wght@500;600&family=Montserrat:wght@400;500&display=swap">
<style>
  :root {
    --brown: #3d1f1e;
    --gold: #f5b22f;
    --white: #ffffff;
    --ink: #2e2e2e;
    --black: #000000;
    --serif: "Cinzel", "Times New Roman", serif;
    --sans: "Montserrat", Arial, sans-serif;
  }
  * { box-sizing: border-box; margin: 0; padding: 0; }
  html, body { width: 1118px; height: 1200px; overflow: hidden; background: var(--white); }
  .sheet { position: relative; width: 1118px; height: 1200px; }

  .option-label {
    position: absolute; left: 42px;
    font: 400 32px/1 var(--sans); color: var(--ink);
  }

  .card {
    position: absolute; width: 484px; height: 295px;
    background: var(--brown); overflow: hidden;
  }
  .card .half-gold { position: absolute; top: 0; right: 0; width: 242px; height: 100%; background: var(--gold); }

  .rule { position: absolute; left: 16px; right: 16px; height: 4px; display: flex; }
  .rule.top { top: 17px; }
  .rule.bottom { bottom: 17px; }
  .rule span { flex: 1; }
  .rule .on-dark { background: var(--gold); }
  .rule .on-gold { background: var(--brown); }

  .mark-square { display: block; margin: 0 auto; }
  .wordmark {
    font-family: var(--serif); font-weight: 500; text-align: center;
    letter-spacing: 2px; white-space: nowrap;
  }

  .framed-logo { position: absolute; width: 124px; height: 180px; padding: 5px; }
  .framed-logo .frame-inner {
    width: 100%; height: 100%; border: 2px solid var(--brown);
    display: flex; flex-direction: column; align-items: center; justify-content: center; gap: 18px;
  }
  .framed-logo.light { background: var(--white); }
  .framed-logo.warm { background: var(--gold); }
  .framed-logo .mark-square { width: 64px; height: 64px; background: var(--brown); }
  .framed-logo .wordmark { font-size: 12px; color: var(--brown); letter-spacing: 1px; }

  .open-logo { position: absolute; width: 160px; text-align: center; }
  .open-logo .mark-square { width: 75px; height: 75px; background: var(--white); }
  .open-logo .wordmark { color: var(--white); font-size: 19px; margin-top: 22px; }

  .details { position: absolute; left: 242px; width: 242px; top: 0; height: 100%; color: var(--brown); }
  .details .heading { position: absolute; left: 0; right: 0; text-align: center; white-space: nowrap; }
  .details.classic .heading { font: 500 24px/1 var(--serif); letter-spacing: 0.5px; }
  .details.classic .heading.sub { font-size: 18px; }
  .details.modern .heading { font: 400 21px/1 var(--sans); letter-spacing: 2px; }
  .details.modern .heading.sub { font: 500 13px/1 var(--serif); letter-spacing: 0.5px; }

  .since {
    position: absolute; left: 0; right: 0; display: flex; align-items: center; justify-content: center; gap: 8px;
    font: 500 6px/1 var(--serif); letter-spacing: 0.5px;
  }
  .since::before, .since::after { content: ""; width: 36px; height: 1px; background: var(--brown); }

  .contact-list { position: absolute; left: 31px; list-style: none; }
  .contact-list li {
    display: flex; align-items: center; gap: 5px; height: 19px;
    font: 400 10.5px/1 var(--sans); letter-spacing: 0.4px; color: var(--brown); white-space: nowrap;
  }
  .contact-list svg { width: 13px; height: 13px; flex: none; }

  .feedback-band {
    position: absolute; left: 0; top: 1054px; width: 1118px; height: 146px;
    background: var(--black); border-top: 1px solid #555;
  }
  .feedback-band p {
    position: absolute; left: 26px; top: 42px;
    font: 400 20px/1 var(--sans); color: var(--white);
  }
</style>
</head>
<body>
<main class="sheet">

  <h2 class="option-label" style="top:201px">OPTION 1</h2>

  <section class="card" style="left:43px; top:248px">
    <div class="half-gold"></div>
    <div class="rule top"><span class="on-dark"></span><span class="on-gold"></span></div>
    <div class="rule bottom"><span class="on-dark"></span><span class="on-gold"></span></div>
    <div class="framed-logo light" style="left:59px; top:58px">
      <div class="frame-inner">
        <span class="mark-square"></span>
        <span class="wordmark">BELLWETHER</span>
      </div>
    </div>
    <div class="details classic">
      <p class="heading" style="top:76px">RESTAURANT</p>
      <p class="heading" style="top:107px">BELLWETHER</p>
      <p class="heading sub" style="top:138px">MAGNOLIA 418</p>
      <p class="since" style="top:160px">Desde 1999</p>
      <ul class="contact-list" style="top:193px">
        <li><svg viewBox="0 0 14 14"><circle cx="7" cy="7" r="7" fill="#3d1f1e"/><path d="M3.5 7.2 7 4l3.5 3.2H9.6V10H8V8.2H6V10H4.4V7.2z" fill="#fff"/></svg>Bahia Serena, Costa Azul</li>
        <li><svg viewBox="0 0 14 14"><circle cx="7" cy="7" r="7" fill="#3d1f1e"/><rect x="3.6" y="6.2" width="6.8" height="3.8" rx="0.8" fill="#fff"/><path d="M3.4 5.6c1.8-1.6 5.4-1.6 7.2 0" stroke="#fff" stroke-width="1.2" fill="none"/></svg>Reservaciones 555-014-2290</li>
        <li><svg viewBox="0 0 14 14"><circle cx="7" cy="7" r="7" fill="#3d1f1e"/><circle cx="7" cy="7" r="3.6" fill="none" stroke="#fff" stroke-width="1"/><path d="M3.4 7h7.2M7 3.4c-1.8 2.2-1.8 5 0 7.2M7 3.4c1.8 2.2 1.8 5 0 7.2" stroke="#fff" stroke-width="0.8" fill="none"/></svg>www.bellwether.com.mx</li>
      </ul>
    </div>
  </section>

  <section class="card" style="left:590px; top:247px">
    <div class="rule top"><span class="on-dark"></span></div>
    <div class="rule bottom"><span class="on-dark"></span></div>
    <div class="open-logo" style="left:162px; top:79px">
      <span class="mark-square"></span>
      <p class="wordmark">BELLWETHER</p>
    </div>
  </section>

  <h2 class="option-label" style="top:607px">OPTION 2</h2>

  <section class="card" style="left:43px; top:653px">
    <div class="half-gold"></div>
    <div class="rule top"><span class="on-dark"></span><span class="on-gold"></span></div>
    <div class="rule bottom"><span class="on-dark"></span><span class="on-gold"></span></div>
    <div class="open-logo" style="left:41px; top:79px">
      <span class="mark-square"></span>
      <p class="wordmark">BELLWETHER</p>
    </div>
    <div class="details modern">
      <p class="heading" style="top:50px">RESTAURANT</p>
      <p class="heading" style="top:77px">BELLWETHER</p>
      <p class="heading sub" style="top:106px">MAGNOLIA 418</p>
      <ul class="contact-list" style="top:180px; left:32px">
        <li><svg viewBox="0 0 14 14"><circle cx="7" cy="7" r="7" fill="#3d1f1e"/><path d="M3.5 7.2 7 4l3.5 3.2H9.6V10H8V8.2H6V10H4.4V7.2z" fill="#fff"/></svg>Bahia Serena, Costa Azul</li>
        <li><svg viewBox="0 0 14 14"><circle cx="7" cy="7" r="7" fill="#3d1f1e"/><rect x="3.6" y="6.2" width="6.8" height="3.8" rx="0.8" fill="#fff"/><path d="M3.4 5.6c1.8-1.6 5.4-1.6 7.2 0" stroke="#fff" stroke-width="1.2" fill="none"/></svg>Reservaciones 555-014-2290</li>
        <li><svg viewBox="0 0 14 14"><circle cx="7" cy="7" r="7" fill="#3d1f1e"/><circle cx="7" cy="7" r="3.6" fill="none" stroke="#fff" stroke-width="1"/><path d="M3.4 7h7.2M7 3.4c-1.8 2.2-1.8 5 0 7.2M7 3.4c1.8 2.2 1.8 5 0 7.2" stroke="#fff" stroke-width="0.8" fill="none"/></svg>www.bellwether.com.mx</li>
      </ul>
    </div>
  </section>

  <section class="card" style="left:590px; top:653px">
    <div class="half-gold"></div>
    <div class="rule top"><span class="on-dark"></span><span class="on-gold"></span></div>
    <div class="rule bottom"><span class="on-dark"></span><span class="on-gold"></span></div>
    <div class="framed-logo warm" style="left:180px; top:56px">
      <div class="frame-inner">
        <span class="mark-square"></span>
        <span class="wordmark">BELLWETHER</span>
      </div>
    </div>
  </section>

  <footer class="feedback-band">
    <p>Any feedback/ rating would be very helpfull.</p>
  </footer>

</main>
</body>
</html>
```